New web page design for our brand Casa Lunares

We have changed our logo and the image of our products, so we would like to redesign ,our web page as well according to the new design.
Our cosmetic products are based in nature and tradition, like they used to be prepared in the old pharmacies.
Our actual web is www.casalunaresweb.es, so we need similar estructure but completely different design.

Industry/Entity Type

Cosmetics

Number of Pages Required

5+ page

Requirements
Must have
• References to natural ingredients and also to old pharmacys or apothecaries.
Nice to have
• Nature images or old botanics drawings
• I would like to have a cover page with just an image saying welcome to Casa Lunares's world

```html
<!DOCTYPE html>
<html lang="es">
<head>
<meta charset="utf-8">
<title>Casa Lunares — Cosmética natural de botica</title>
<link href="https://fonts.googleapis.com/css2?family=Playfair+Display:wght@400;700&family=Open+Sans:wght@400;600;700&display=swap" rel="stylesheet">
<style>
:root{
  --ink:#2b2b2b;
  --text:#555;
  --muted:#888;
  --paper:#fff;
  --band:#efefef;
  --button:#4a4a4a;
  --footer:#202020;
  --footer-base:#161616;
  --footer-text:#9a9a9a;
  --hero-a:#6b5a45;
  --hero-b:#a89276;
  --accent:#8a6d3b;
}
*{box-sizing:border-box;margin:0;padding:0}
html,body{width:1200px;height:2612px;overflow:hidden}
body{background:var(--paper);font-family:"Open Sans",Arial,sans-serif;color:var(--text);font-size:13px;line-height:1.6}
h2{font-family:"Playfair Display",Georgia,serif;font-weight:400;color:var(--ink);text-align:center;font-size:30px;line-height:1.3}

/* header */
.site-header{height:100px;position:relative}
.brand{position:absolute;left:100px;top:26px;display:flex;align-items:center;gap:12px}
.brand-mark{width:16px;height:16px;background:var(--accent)}
.brand-name{font-family:"Playfair Display",Georgia,serif;font-weight:700;font-size:30px;line-height:1.3;color:var(--ink)}
.topbar{position:absolute;right:100px;top:12px;display:flex;align-items:center;gap:26px;font-size:12px;color:var(--muted)}
.topbar span{display:flex;align-items:center;gap:8px}
.main-nav{position:absolute;right:100px;top:56px;display:flex;gap:40px;font-size:12px;letter-spacing:.5px;text-transform:uppercase;color:var(--muted)}
.main-nav a{color:inherit;text-decoration:none;padding-bottom:6px}
.main-nav a.active{color:var(--ink);font-weight:700;border-bottom:2px solid var(--ink)}

/* hero */
.hero{height:660px;position:relative;background:linear-gradient(120deg,var(--hero-a),var(--hero-b) 55%,#7c6a52)}
.hero-caption{position:absolute;right:100px;top:360px;text-align:right}
.hero-caption span{display:inline-block;background:rgba(0,0,0,.55);color:#fff;font-weight:700;font-size:32px;line-height:1.25;padding:4px 14px;margin-top:4px}

/* welcome */
.welcome{padding:36px 148px 0;height:400px}
.welcome p.lead{margin:20px 0 36px;text-align:justify;font-size:12px;line-height:1.75}
.features{display:flex;gap:24px}
.feature{flex:1;display:flex;gap:14px}
.feature-img{width:120px;height:104px;flex:none;background:linear-gradient(135deg,#efe3d3,#d9b99b)}
.feature h3{font-size:14px;color:var(--ink);font-weight:600;margin-bottom:4px}
.feature p{font-size:11px;line-height:1.6}
.feature .more{display:block;text-align:right;font-size:11px;color:var(--ink);margin-top:6px}

/* products */
.products{background:var(--band);height:500px;position:relative;padding-top:40px}
.product-row{display:flex;gap:16px;margin:34px 0 0 108px}
.product{width:184px;background:var(--paper);text-align:center;padding-bottom:16px}
.product-img{height:140px;background:linear-gradient(180deg,#f3f7ef,#dde9d6)}
.product h3{font-size:14px;color:var(--ink);font-weight:600;margin:12px 0 4px}
.product p{font-size:10.5px;line-height:1.55;padding:0 12px;height:66px;overflow:hidden}
.btn{display:inline-block;background:var(--button);color:#fff;font-size:11px;padding:4px 16px;margin-top:8px}
.arrow{position:absolute;top:250px;width:30px;height:40px;background:#9a9a9a;display:flex;align-items:center;justify-content:center}
.arrow.prev{left:0}.arrow.next{right:0}

/* what we do */
.what{padding:36px 152px 0;height:600px}
.what p.lead{margin:18px 0 28px;text-align:center;font-size:12px;line-height:1.75}
.services{display:flex;gap:40px}
.service{flex:1;text-align:center}
.service-img{height:230px}
.service h3{font-family:"Playfair Display",Georgia,serif;font-weight:400;font-size:24px;line-height:1.3;color:var(--ink);margin:12px 0 8px}
.service p{font-size:11.5px;line-height:1.7}

/* footer */
.site-footer{background:var(--footer);height:320px;color:var(--footer-text);display:flex;padding:36px 100px 0;font-size:11.5px}
.site-footer h4{color:#fff;font-size:14px;font-weight:600;margin-bottom:18px}
.col-news{width:320px}
.col-menu{width:192px}
.col-contact{width:260px}
.col-quick{width:228px}
.site-footer li{list-style:none;margin-bottom:12px;display:flex;gap:10px;align-items:flex-start}
.bullet{width:5px;height:5px;border-radius:50%;background:#777;margin-top:7px;flex:none}
.social{display:flex;gap:12px;margin-top:6px}
.social i{width:16px;height:16px;border-radius:50%;background:#555;display:block}
.field{background:#3a3a3a;height:26px;margin-bottom:8px}
.field.area{height:60px}
.send{display:inline-block;background:#eee;color:#333;font-size:11px;padding:3px 14px}
.copyright{background:var(--footer-base);height:32px;text-align:center;color:#777;font-size:10px;line-height:32px;letter-spacing:.5px}
</style>
</head>
<body>

<header class="site-header">
  <div class="brand"><span class="brand-mark"></span><span class="brand-name">Casa Lunares</span></div>
  <div class="topbar">
    <span><svg width="14" height="14" viewBox="0 0 24 24"><path fill="#777" d="M6.6 10.8a15 15 0 0 0 6.6 6.6l2.2-2.2c.3-.3.7-.4 1-.2 1.1.4 2.3.6 3.6.6.6 0 1 .4 1 1V20c0 .6-.4 1-1 1A17 17 0 0 1 3 4c0-.6.4-1 1-1h3.5c.6 0 1 .4 1 1 0 1.3.2 2.5.6 3.6.1.3 0 .7-.2 1z"/></svg>+34 600 123 456</span>
    <span><svg width="16" height="14" viewBox="0 0 24 20"><path fill="none" stroke="#777" stroke-width="2" d="M1 2h4l3 11h12l3-8H7"/><circle cx="9" cy="17" r="1.6" fill="#777"/><circle cx="19" cy="17" r="1.6" fill="#777"/></svg>Tu carrito</span>
  </div>
  <nav class="main-nav">
    <a class="active" href="#">Laboratorio</a><a href="#">Línea de productos</a><a href="#">Servicio</a><a href="#">Noticias</a><a href="#">Contacto</a><a href="#">Tienda</a>
  </nav>
</header>

<section class="hero" role="img" aria-label="Amber apothecary bottle of almond oil on a rustic wooden table with bowls of oils, herbs and rosemary">
  <div class="hero-caption"><span>Lorem ipsum dolor sit amet,</span><br><span>consectetur adipiscing</span></div>
</section>

<section class="welcome">
  <h2>Welome To Our Site</h2>
  <p class="lead">Lorem ipsum dolor sit amet, consectetur adipiscing elit. Proin ultrices mauris lectus, at tincidunt nibh feugiat eu. Phasellus et hendrerit dolor. Morbi justo risus, pulvinar ac volutpat ut, consequat nec erat. Curabitur et malesuada lorem, ut cursus ipsum pretium at tincidunt. Vestibulum ante ipsum primis in faucibus orci luctus et ultrices posuere cubilia. Donec at ipsum at vestibulum finibus. Morbi ligula odio, consequat non nisi id, porta consectetur metus. Sed vitae magna sed dui aliquet lacinia pellentesque et non. Nam elit turpis, sollicitudin quis, eget bibendum leo dapibus ut. Sed et tortor ac ipsum finibus gravida sed, pretium dolor.</p>
  <div class="features">
    <div class="feature">
      <div class="feature-img" role="img" aria-label="Vintage illustrated product label with floral border"></div>
      <div><h3>Línea Premium</h3><p>La línea Premium de Casa Lunares combina los activos naturales más valiosos con recetas clásicas para el cuidado diario de la piel.</p><span class="more">Read More »</span></div>
    </div>
    <div class="feature">
      <div class="feature-img" role="img" aria-label="Jars of baby care cream beside a painted cherub figure" style="background:linear-gradient(135deg,#f6efe3,#e2c9a4)"></div>
      <div><h3>Línea Infantil</h3><p>La línea Infantil de Casa Lunares está especialmente pensada para la piel delicada de los más pequeños de la casa.</p><span class="more">Read More »</span></div>
    </div>
    <div class="feature">
      <div class="feature-img" role="img" aria-label="Old pharmacy counter with glass jars" style="background:linear-gradient(135deg,#ece6dc,#c9b79c)"></div>
      <div><h3>Línea Botica</h3><p>Fórmulas tradicionales de la antigua botica, preparadas con ingredientes naturales y mucho mimo.</p><span class="more">Read More »</span></div>
    </div>
  </div>
</section>

<section class="products">
  <h2>Our Products</h2>
  <div class="product-row">
    <div class="product"><div class="product-img" role="img" aria-label="Row of essential oil bottles with botanical labels"></div><h3>Tratamiento de cara</h3><p>Rutina facial con aceites y cremas de origen natural para nutrir y proteger la piel.</p><span class="btn">View More</span></div>
    <div class="product"><div class="product-img" role="img" aria-label="Aromatic cosmetic bottles with herbal labels"></div><h3>Línea Aromática</h3><p>Esencias puras de lavanda, romero y azahar elaboradas según recetas de botica.</p><span class="btn">View More</span></div>
    <div class="product"><div class="product-img" role="img" aria-label="Moisturising cream jars"></div><h3>Cosmética</h3><p>Cremas hidratantes y bálsamos suaves con manteca de karité y aceite de almendras.</p><span class="btn">View More</span></div>
    <div class="product"><div class="product-img" role="img" aria-label="Dermatological care bottles"></div><h3>Línea Dermática</h3><p>Cuidados específicos para pieles sensibles con extractos calmantes de plantas.</p><span class="btn">View More</span></div>
    <div class="product"><div class="product-img" role="img" aria-label="Set of natural body care products"></div><h3>Cuidado corporal</h3><p>Aceites corporales y jabones artesanos para el ritual diario de bienestar.</p><span class="btn">View More</span></div>
  </div>
  <span class="arrow prev"><svg width="10" height="14" viewBox="0 0 10 14"><path d="M8 1 2 7l6 6" fill="none" stroke="#fff" stroke-width="2"/></svg></span>
  <span class="arrow next"><svg width="10" height="14" viewBox="0 0 10 14"><path d="m2 1 6 6-6 6" fill="none" stroke="#fff" stroke-width="2"/></svg></span>
</section>

<section class="what">
  <h2>What We Do</h2>
  <p class="lead">Sed sollicitudin, lacus eget ultrices imperdiet, nibh turpis sagittis lectus, eget tristique erat ipsum at lacus. In auctor malesuada turpis, convallis euismod ante pulvinar vel. Duis volutpat feugiat nunc, in hendrerit nunc pretium a. Etiam dolor arcu, tincidunt nec vestibulum vel. Nulla facilisi. Donec ultricies lacus eget vulputate tempor, mauris quam porttitor nisi in maximus. Nulla mollis purus vel odio pulvinar, eu volutpat nisl porta.</p>
  <div class="services">
    <div class="service">
      <div class="service-img" role="img" aria-label="Bottles of oil with fresh herbs, olives and spices on a wooden table" style="background:linear-gradient(135deg,#5a4632,#9c7f57 60%,#6d7a3e)"></div>
      <h3>Natural Ingredients</h3>
      <p>Sed sollicitudin, lacus eget ultrices imperdiet, nibh turpis sagittis lectus, eget tristique erat ipsum at lacus. In auctor malesuada turpis, convallis euismod ante pulvinar vel. Duis volutpat feugiat nunc.</p>
    </div>
    <div class="service">
      <div class="service-img" role="img" aria-label="Pharmacists attending in a bright pharmacy with shelves of products" style="background:linear-gradient(135deg,#dfe6ec,#9fb2c3 60%,#c9d3da)"></div>
      <h3>Apothecaries</h3>
      <p>Sed sollicitudin, lacus eget ultrices imperdiet, nibh turpis sagittis lectus, eget tristique erat ipsum at lacus. In auctor malesuada turpis, convallis euismod ante pulvinar vel. Duis volutpat feugiat nunc.</p>
    </div>
  </div>
</section>

<footer class="site-footer">
  <div class="col-news">
    <h4>Recent News</h4>
    <ul>
      <li><span class="bullet"></span>Nuevas recetas para tu piel</li>
      <li><span class="bullet"></span>Lorem ipsum is all about quality</li>
      <li><span class="bullet"></span>Los secretos de la antigua botica</li>
      <li><span class="bullet"></span>Aceites naturales para el invierno</li>
      <li><span class="bullet"></span>Tus productos favoritos, ahora online</li>
    </ul>
  </div>
  <div class="col-menu">
    <h4>Menu</h4>
    <ul><li>Inicio</li><li>Nosotros</li><li>Servicio</li><li>Tienda</li><li>Contacto</li></ul>
  </div>
  <div class="col-contact">
    <h4>Contact Info</h4>
    <ul>
      <li><span class="bullet"></span>hola@casalunaresweb.es</li>
      <li><span class="bullet"></span>+34 600 123 456</li>
      <li><span class="bullet"></span>C/ del Romero 12, Valdeluz</li>
    </ul>
    <div class="social"><i></i><i></i><i></i><i></i></div>
  </div>
  <div class="col-quick">
    <h4>Quick Contact</h4>
    <div class="field"></div>
    <div class="field"></div>
    <div class="field area"></div>
    <span class="send">Send</span>
  </div>
</footer>
<div class="copyright">© COPYRIGHT 2015 CASA LUNARES. ALL RIGHTS RESERVED.</div>

</body>
</html>
```